Qorvel Consulting

We focus on Data Recovery but we also do Network Security. We recover data from all types of hard drive form factors 3.5", 2.5", 1", 1.8", 5.25", 8" with any kind of interface IDE(PATA), SATA, mSATA, SCSI, SAS and Fibre Channel. All RAID Arrays 0, 1, 2, 3, 4, 5, 10 including nested levels like RAID 0+1, 1+0, 100, 0+3, 50 and 60, flash drives, like tablets, cellphones, usb drives, memory cards(SD, miniSD, Data Wafer(tavik))

Actually you can gather any information or text from any data recovery site, cause is usually the same info, we would probably change a couple of things from the description so it wont look the same. One thing though, we want to make clear to users not to attempt data recovery themselves and to ship the faulty device to us, maybe we can illustrate this?

the Data Recovery link can have sub menus like "Data Recovery Process - Data Recovery Services - F.A.Q"

the Penetration Testing can have sub menus like "F.A.Q - Pentest Process - Pentest Services"

Here are links from website so you gather information:

-http://www.mydiskwentdark.example/

-http://www.bitrescuelabsrecovery.example/

-http://www.pulvenbytes.example/

http://fetchlostfiles.example/lp/hard-drive-recovery.aspx?src=Brovix&gclid=ZTRWq4XplnQMDA-kwPbcf7HE2s
http://www.qulm.example/
http://www.venbrisfield.example/data-recovery/
http://www.tzwdatarecovery.example/

thanks.

Target Market(s)

Any PC user

Industry/Entity Type

Data Recovery

Requirements
Must have
• - Language and geographic navigation
- Home page navigation
- Global navigation
- Breadcrumbs
Nice to have
• - Sliders
-Drop down navigation

```html
<!DOCTYPE html>
<html lang="en">
<head>
<meta charset="utf-8">
<title>Qorvel Consulting – Data Recovery</title>
<link href="https://fonts.googleapis.com/css2?family=Roboto+Condensed:wght@300;400;700&family=Arimo:wght@400;700&display=swap" rel="stylesheet">
<style>
:root{
  --red:#e31b23;
  --red-dark:#c8102e;
  --black:#161616;
  --nav:#1b1b1b;
  --page:#f2f2f2;
  --text:#3a3a3a;
  --muted:#6b6b6b;
  --line:#d9d9d9;
  --white:#ffffff;
  --icon:#2a2a2a;
  --icon-light:#9a9a9a;
}
*{box-sizing:border-box;margin:0;padding:0}
html,body{width:935px;height:1200px;overflow:hidden}
body{background:var(--page);font-family:"Arimo",Arial,sans-serif;color:var(--text);position:relative}
.abs{position:absolute}

.topbar{left:0;top:0;width:935px;height:18px;background:var(--red)}
.topbar-tab{left:700px;top:0;width:235px;height:30px;background:var(--red);clip-path:polygon(0 0,100% 0,100% 100%,8px 100%)}
.topbar-msg{left:114px;top:4px;font-size:8px;font-weight:700;color:var(--white);letter-spacing:.1px}
.lang{left:714px;top:2px;width:88px;height:23px;background:var(--white);display:flex;align-items:center;font-family:"Roboto Condensed",sans-serif;font-size:8px;color:var(--muted)}
.lang .flag{width:14px;height:9px;background:#2b3f87;margin:0 6px;border:1px solid #c22}
.lang .caret{margin-left:auto;width:20px;height:100%;border-left:1px solid var(--line);display:flex;align-items:center;justify-content:center}

.brand{left:108px;top:40px;font-family:"Roboto Condensed",sans-serif;font-weight:700;color:var(--nav);font-size:30px;line-height:1;display:flex;align-items:center;gap:6px}
.brand .dot{width:12px;height:12px;background:var(--red)}
.brand small{display:block;font-size:11px;color:var(--red);font-weight:700;letter-spacing:1px;margin-top:2px}
.contact{right:132px;top:52px;text-align:right;font-family:"Roboto Condensed",sans-serif;font-size:10px;color:var(--muted);line-height:19px}

.nav{left:94px;top:108px;width:748px;height:38px;background:var(--nav);display:flex;box-shadow:0 2px 4px rgba(0,0,0,.2)}
.nav a{font-family:"Roboto Condensed",sans-serif;font-weight:700;font-size:10.5px;color:var(--white);text-decoration:none;display:flex;align-items:center;padding:0 19px;border-right:1px solid #333}
.nav a.active{background:var(--red);padding:0 25px}
.nav .search{margin-left:auto;width:210px;background:var(--red);display:flex;align-items:center;justify-content:center}
.nav .search span{width:189px;height:24px;background:var(--white);display:flex;justify-content:flex-end;align-items:center;padding-right:5px}

.crumbs{left:94px;top:156px;font-size:9px;color:var(--muted)}
.crumbs b{color:#c4c4c4;margin-left:6px;font-weight:400}

.hero{left:94px;top:176px;width:748px;height:308px;overflow:hidden;
  background:
    radial-gradient(ellipse 90px 80px at 24% 68%,rgba(150,215,240,.75),rgba(60,150,195,.35) 55%,transparent 100%),
    radial-gradient(ellipse 260px 230px at 26% 60%,rgba(25,95,135,.9),transparent 75%),
    radial-gradient(ellipse 160px 300px at 52% 35%,rgba(150,185,205,.45),transparent 70%),
    linear-gradient(100deg,#06121b 0%,#0d2e44 28%,#3d6f8c 58%,#587f98 100%)}
.hero-tag{position:absolute;left:410px;font-family:"Roboto Condensed",sans-serif;font-weight:400;font-size:34px;line-height:38px;padding:0 9px;white-space:nowrap}
.tag1{top:92px;background:var(--red);color:var(--nay,#1b1b1b);width:194px}
.tag2{top:135px;background:var(--nav);color:var(--red);width:278px}
.dots{position:absolute;right:26px;bottom:14px;display:flex;gap:6px}
.dots i{width:10px;height:10px;border-radius:50%;background:#333;border:1px solid #888}
.dots i:first-child{background:#eee}

.features{left:93px;top:502px;display:flex;gap:12px}
.feature{width:243px;height:82px;background:var(--white);border:1px solid var(--line);display:flex;padding:9px 8px 0 6px;gap:10px}
.feature svg{flex:none;margin-top:4px}
.feature h3{font-family:"Roboto Condensed",sans-serif;font-weight:400;color:var(--red);font-size:15px;letter-spacing:-.4px;margin-bottom:6px}
.feature p{font-size:8.6px;line-height:12.5px;text-align:justify}

.divider{left:35px;width:865px;height:1px;background:var(--line)}
.h2{font-family:"Roboto Condensed",sans-serif;font-weight:400;color:#444;font-size:16px;letter-spacing:-.4px}
.rule{height:1px;background:var(--line)}

.welcome-photo{left:93px;top:670px;width:209px;height:163px;border:4px solid var(--white);box-shadow:0 0 3px rgba(0,0,0,.3);
  background:
    radial-gradient(ellipse 70px 50px at 62% 78%,rgba(235,238,242,.95),rgba(170,180,190,.6) 60%,transparent 100%),
    radial-gradient(ellipse 50px 60px at 28% 30%,rgba(230,230,235,.6),transparent 80%),
    linear-gradient(165deg,#1e3560 0%,#3d5f93 40%,#7e9bc4 70%,#b9c4d2 100%)}
.welcome-text{left:309px;top:667px;width:230px;font-size:9.2px;line-height:14px;text-align:justify}
.welcome-text .lead{color:var(--red-dark);margin-bottom:14px;text-align:left}

.video{left:554px;top:661px;width:292px;height:182px;background:var(--white);padding:5px}
.video .screen{width:100%;height:100%;background:radial-gradient(circle at 50% 45%,#a9cde0,#5c93b3 60%,#3f7191);border:2px solid #1c2b36;position:relative}
.video .bar{position:absolute;left:0;right:0;bottom:0;height:14px;background:#16222b;display:flex;align-items:center;gap:3px;padding:0 3px;font-size:5px;color:#ccc}
.video .bar i{width:7px;height:7px;border-radius:50%;background:#7fa3bb}
.video .track{flex:1;height:2px;background:#3b4d5a;margin:0 4px}

.services{left:95px;top:917px;display:flex;gap:31px}
.service{width:98px;height:97px;background:var(--white);border:1px solid #e3e3e3;display:flex;flex-direction:column;align-items:center;padding-top:17px}
.service svg{width:46px;height:46px}
.service span{margin-top:16px;font-family:"Roboto Condensed",sans-serif;font-weight:700;font-size:8.5px;color:var(--red)}

.partners{left:94px;top:1038px;width:748px;height:88px;background:#f7f7f7;border:1px solid #e3e3e3;display:flex;align-items:center;justify-content:space-around;padding:0 6px}
.partners span{font-family:"Roboto Condensed",sans-serif;font-weight:700;font-size:21px;color:#5a5a5a}

.footer{left:0;top:1146px;width:935px;height:54px;background:var(--black)}
.footer .copy{position:absolute;left:94px;top:20px;font-size:9px;color:#d0d0d0}
.footer .social{position:absolute;left:698px;top:8px;display:flex;gap:7px}
.footer .social i{width:24px;height:24px;border-radius:50%;background:#4a4a4a}
.footer .code{position:absolute;right:8px;top:20px;font-size:10px;color:#e0e0e0}
</style>
</head>
<body>
<div class="abs topbar"></div>
<div class="abs topbar-tab"></div>
<div class="abs topbar-msg">Got Questions? We've got answers! LIVE CHAT WITH A SPECIALIST NOW!</div>
<div class="abs lang"><span class="flag" role="img" aria-label="English flag"></span>ENGLISH<span class="caret"><svg width="7" height="6"><path d="M0 0h7L3.5 6z" fill="#999"/></svg></span></div>

<div class="abs brand"><span class="dot"></span><div>Qorvel<small>CONSULTING</small></div></div>
<div class="abs contact">CALL US: 000.000.0000<br>OUR INTERNATIONAL NUMBERS</div>

<nav class="abs nav">
  <a class="active" href="#">HOME</a>
  <a href="#">DATA RECOVERY PROCESS</a>
  <a href="#">DATA RECOVERY SERVICES</a>
  <a href="#">FAQ</a>
  <a href="#">CONTACT</a>
  <div class="search"><span><svg width="10" height="10" viewBox="0 0 10 10"><circle cx="4" cy="4" r="2.8" fill="none" stroke="#3b5ba5" stroke-width="1.2"/><path d="M6 6l3 3" stroke="#3b5ba5" stroke-width="1.4"/></svg></span></div>
</nav>

<div class="abs crumbs">Home<b>&gt;</b></div>

<section class="abs hero" role="img" aria-label="Close-up of an open hard drive platter and read arm in blue light">
  <div class="hero-tag tag1">YOUR 24/7</div>
  <div class="hero-tag tag2">RECOVERY HEROES</div>
  <div class="dots"><i></i><i></i><i></i><i></i></div>
</section>

<div class="abs features">
  <div class="feature">
    <svg width="60" height="60" viewBox="0 0 60 60" role="img" aria-label="Hard drive icon"><rect x="6" y="12" width="48" height="36" rx="4" fill="#d8d2c6" stroke="#6d6659" stroke-width="2"/><circle cx="26" cy="30" r="12" fill="#ece9e3" stroke="#8b8478" stroke-width="1.5"/><circle cx="26" cy="30" r="3" fill="#6d6659"/><path d="M46 18L32 34" stroke="#3b3b3b" stroke-width="3" stroke-linecap="round"/></svg>
    <div><h3>DEVICES SUPPORTED</h3><p>ullamco laboris nisi ut aliquip ex ea commodo consequat. Duis aute irure dolor in reprehenderit in voluptate velit</p></div></div>
  <div class="feature">
    <svg width="60" height="60" viewBox="0 0 60 60" role="img" aria-label="Wastebasket icon"><path d="M14 20h32l-4 32H18z" fill="#eeeeee" stroke="#555" stroke-width="2"/><path d="M22 24l2 24M30 24v24M38 24l-2 24" stroke="#777" stroke-width="1.5"/><rect x="12" y="16" width="36" height="5" rx="2" fill="#888"/><rect x="20" y="8" width="8" height="9" fill="#e31b23"/><rect x="30" y="6" width="9" height="11" fill="#3b6fb5"/></svg>
    <div><h3>DATA FILE RECOVERY</h3><p>ullamco laboris nisi ut aliquip ex ea commodo consequat. Duis aute irure dolor in reprehenderit in voluptate velit</p></div></div>
  <div class="feature">
    <svg width="60" height="60" viewBox="0 0 60 60" role="img" aria-label="Server stack icon"><rect x="14" y="8" width="32" height="14" rx="3" fill="#d0d0d0" stroke="#888" stroke-width="1.5"/><rect x="14" y="24" width="32" height="12" rx="2" fill="#c4c4c4" stroke="#888" stroke-width="1.5"/><rect x="14" y="38" width="32" height="12" rx="2" fill="#b8b8b8" stroke="#888" stroke-width="1.5"/><path d="M18 30h24M18 44h24" stroke="#777"/></svg>
    <div><h3>RAID RECOVERY</h3><p>ullamco laboris nisi ut aliquip ex ea commodo consequat. Duis aute irure dolor in reprehenderit in voluptate velit</p></div></div>
</div>

<div class="abs divider" style="top:600px"></div>

<div class="abs h2" style="left:93px;top:617px">WELCOME</div>
<div class="abs rule" style="left:93px;top:649px;width:445px"></div>
<div class="abs h2" style="left:560px;top:617px">HOW IT WORKS</div>
<div class="abs rule" style="left:560px;top:649px;width:282px"></div>

<div class="abs welcome-photo" role="img" aria-label="Technician holding an open hard drive in a lab"></div>
<div class="abs welcome-text">
  <p class="lead">Sed ut perspiciatis unde omnis iste natus error sit voluptatem accusantium doloremque laudantium, totam rem aperiam</p>
  <p>&nbsp;eaque ipsa quae ab illo inventore veritatis et quasi architecto beatae vitae dicta sunt explicabo. Nemo enim ipsam voluptatem quia voluptas sit aspernatur aut odit aut fugit, sed quia consequuntur magni dolores eos qui ratione voluptatem sequi nesciunt. Neque porro quisquam est, qui dolorem ipsum quia dolor sit amet, consectetur, adipisci velit, sed quia non numquam eius modi tempora incidunt ut labore et dolore magnam</p>
</div>

<div class="abs video">
  <div class="screen">
    <svg class="abs" style="left:114px;top:56px" width="54" height="54" viewBox="0 0 54 54"><circle cx="27" cy="27" r="24" fill="rgba(255,255,255,.15)" stroke="rgba(255,255,255,.6)" stroke-width="3"/><path d="M21 16v22l18-11z" fill="rgba(255,255,255,.6)"/></svg>
    <div class="bar"><i></i><i></i><i></i><span class="track"></span>00:12 / 3:24 HD</div>
  </div>
</div>

<div class="abs divider" style="top:861px"></div>
<div class="abs h2" style="left:94px;top:870px">OUR SERVICES</div>
<div class="abs rule" style="left:94px;top:902px;width:748px"></div>

<div class="abs services">
  <div class="service"><svg viewBox="0 0 46 46" role="img" aria-label="Globe icon"><circle cx="23" cy="23" r="20" fill="none" stroke="var(--icon)" stroke-width="3.5"/><ellipse cx="23" cy="23" rx="8" ry="20" fill="none" stroke="var(--icon)" stroke-width="2"/><path d="M3 23h40M7 13h32M7 33h32" stroke="var(--icon)" stroke-width="2"/></svg><span>INTERNATIONAL</span></div>
  <div class="service"><svg viewBox="0 0 46 46" role="img" aria-label="Flash drive icon"><rect x="6" y="16" width="26" height="16" rx="3" fill="var(--icon)"/><rect x="32" y="19" width="9" height="10" fill="#c8c8c8" stroke="#777"/><path d="M10 19h18" stroke="#666" stroke-width="1.5"/></svg><span>FLASH DRIVES</span></div>
  <div class="service"><svg viewBox="0 0 46 46" role="img" aria-label="Tablet icon"><rect x="3" y="4" width="40" height="38" rx="3" fill="var(--icon)"/><rect x="6" y="8" width="34" height="31" fill="#3a3a3a"/><circle cx="23" cy="6" r="1" fill="#888"/></svg><span>TABLETS</span></div>
  <div class="service"><svg viewBox="0 0 46 46" role="img" aria-label="Cellphone icon"><rect x="12" y="1" width="22" height="44" rx="4" fill="var(--icon)"/><rect x="14" y="6" width="18" height="33" fill="#050505"/><circle cx="23" cy="42" r="1.5" fill="#666"/></svg><span>CELLPHONES</span></div>
  <div class="service"><svg viewBox="0 0 46 46" role="img" aria-label="USB drive icon"><rect x="12" y="2" width="22" height="32" rx="3" fill="var(--icon)"/><rect x="14" y="34" width="18" height="9" fill="#d8d8d8" stroke="#777"/><path d="M23 10v12M20 14l3-4 3 4" stroke="#ccc" stroke-width="1.5" fill="none"/></svg><span>USB DRIVES</span></div>
  <div class="service"><svg viewBox="0 0 46 46" role="img" aria-label="Memory card icon"><rect x="2" y="10" width="42" height="26" rx="2" fill="var(--icon)"/><rect x="5" y="13" width="36" height="7" fill="#8a8a8a"/><path d="M6 30h6M14 30h6M22 30h6" stroke="#aaa" stroke-width="2"/></svg><span>MEMORY CARDS</span></div>
</div>

<div class="abs partners">
  <span>Halvec</span><span>Ordane</span><span>Brevium</span><span>Kestro</span><span>Vantrel</span><span>Soraku</span><span>Pellmar</span>
</div>

<footer class="abs footer">
  <div class="copy">© 2013 Qorvel Consulting. All Rights reserved.</div>
  <div class="social"><i></i><i></i><i></i><i></i></div>
  <div class="code">C2</div>
</footer>
</body>
</html>
```